Intenational Rhythmic Gymnastics Frostline Trophy

We need a poster for our new annual international rhythmic gymnastics competition "Frostline Trophy". Dates are December 21 -23, 2019.Picture we would like to use is attached.We would like to see holidays colors in the poster.It should have words "international rhythmic gymnastics", Name of the competition "Frostline Trophy" and dates.Also we would like for it to say somewhere that it is in Los Angeles, California, USAIt should have information about our club on the bottom of the poster like on the file attached (hosted by Venmarra Gymnastics with logo and address and website info)We also need a flyer that ties into the poster in look and colors with empty space below so we can add directives.We would like end product to be in file format that we can edit next year when the dates change.

Target Market(s)

Rhythmic Gymnastics Clubs

Industry/Entity Type

Gym

Colors

Designer to choose colors to be used in the design.

Requirements
Must have
• Picture we uploaded and all info we requested.
• Bright holiday colors

```html
<!DOCTYPE html>
<html lang="en">
<head>
<meta charset="utf-8">
<title>Frostline Trophy 2019 – International Rhythmic Gymnastics</title>
<link rel="stylesheet" href="https://fonts.googleapis.com/css2?family=Great+Vibes&family=Alex+Brush&family=PT+Serif&family=PT+Sans:wght@400;700&family=Roboto+Condensed:wght@700&display=swap">
<style>
  :root {
    --night-blue: #0d2a78;
    --deep-blue: #071a52;
    --royal-blue: #1f3f9e;
    --ice: #cfe9f8;
    --snow: #ffffff;
    --holly-red: #d8262b;
    --ember: #f08a1c;
    --gold: #f9c623;
    --ribbon-red: #ec5a49;
    --cyan: #18a9e6;
    --ink-navy: #1c2a5e;
    --text-red: #c8202a;
    --page: #e9e9e9;
  }
  * { margin: 0; padding: 0; box-sizing: border-box; }
  html, body { width: 988px; height: 1200px; overflow: hidden; background: var(--page); }
  .poster { position: relative; width: 988px; height: 1200px; overflow: hidden; background: var(--snow); }
  .backdrop { position: absolute; inset: 0; }
  .title {
    position: absolute; left: 44px; top: 28px;
    font-family: "Great Vibes", cursive; font-size: 96px; line-height: 1;
    color: var(--snow); white-space: nowrap;
  }
  .year {
    position: absolute; left: 80px; top: 192px;
    font-family: "PT Serif", serif; font-size: 112px; line-height: 1;
    color: var(--snow);
  }
  .photo {
    position: absolute; left: 160px; top: 330px; width: 560px; height: 770px;
    border-radius: 40% 40% 12% 12%;
    background: radial-gradient(ellipse at 55% 55%, rgba(214,170,140,0.75), rgba(110,80,150,0.45) 45%, rgba(207,233,248,0) 72%);
  }
  .badge { position: absolute; left: 556px; top: 310px; width: 376px; height: 376px; }
  .badge-text {
    position: absolute; left: 556px; top: 310px; width: 376px; height: 376px;
    display: flex; flex-direction: column; align-items: center; justify-content: center;
    color: var(--snow); text-align: center;
  }
  .badge-line1 { font-family: "Roboto Condensed", sans-serif; font-weight: 700; font-size: 38px; line-height: 1; }
  .badge-line2 { font-family: "Alex Brush", cursive; font-size: 62px; line-height: 1.05; }
  .badge-line3 { font-family: "PT Sans", sans-serif; font-weight: 700; font-size: 39px; line-height: 1; }
  .trophy {
    position: absolute; left: 628px; top: 680px; width: 220px; height: 158px;
    border-radius: 30% 30% 45% 45%;
    background: linear-gradient(90deg, #a8731a, #f7d67a 45%, #c68b22 80%, #8a5a10);
  }
  .dates-ribbon { position: absolute; left: 530px; top: 808px; width: 430px; height: 110px; }
  .dates {
    position: absolute; left: 560px; top: 836px; width: 360px;
    transform: rotate(-4deg);
    font-family: "PT Sans", sans-serif; font-weight: 700; font-size: 44px;
    color: var(--snow); text-align: center; white-space: nowrap;
  }
  .footer { position: absolute; left: 0; right: 0; top: 1130px; height: 70px; }
  .hosted-by {
    position: absolute; left: 0; top: 8px; width: 202px; height: 24px;
    background: var(--cyan); color: var(--snow);
    font-family: "PT Sans", sans-serif; font-weight: 700; font-size: 16px; letter-spacing: 3px;
    display: flex; align-items: center; justify-content: flex-end; padding-right: 12px;
  }
  .host {
    position: absolute; left: 220px; top: 0; display: flex; align-items: center; gap: 12px;
    font-family: "PT Sans", sans-serif; font-weight: 400; font-size: 31px; color: var(--ink-navy);
    white-space: nowrap;
  }
  .host-mark { width: 22px; height: 22px; border-radius: 50%; background: var(--ink-navy); }
  .venue {
    position: absolute; left: 604px; top: 0; width: 346px;
    font-family: "PT Sans", sans-serif; color: var(--text-red); font-size: 23px;
    padding-bottom: 5px; border-bottom: 1px solid #b9c4d6; white-space: nowrap;
  }
  .venue .dot { display: inline-block; width: 7px; height: 7px; border-radius: 50%; background: var(--text-red); margin: 0 7px; vertical-align: middle; }
  .website {
    position: absolute; left: 604px; top: 40px;
    font-family: "PT Sans", sans-serif; font-weight: 700; font-size: 20px; letter-spacing: 2px;
    color: var(--ink-navy); white-space: nowrap;
  }
</style>
</head>
<body>
<main class="poster">
  <svg class="backdrop" width="988" height="1200" viewBox="0 0 988 1200" aria-hidden="true">
    <defs>
      <linearGradient id="snowfield" x1="0" y1="0" x2="0" y2="1">
        <stop offset="0" stop-color="#a9d8f2"/>
        <stop offset="0.6" stop-color="#d9eef9"/>
        <stop offset="1" stop-color="#ffffff"/>
      </linearGradient>
      <radialGradient id="starburst" cx="0.58" cy="0.55" r="0.8">
        <stop offset="0" stop-color="#6fa8ee"/>
        <stop offset="0.3" stop-color="#1f3f9e"/>
        <stop offset="1" stop-color="#071a52"/>
      </radialGradient>
      <linearGradient id="emberBand" x1="0" y1="0" x2="1" y2="0">
        <stop offset="0" stop-color="#f08a1c"/>
        <stop offset="0.5" stop-color="#f9c623"/>
        <stop offset="1" stop-color="#f08a1c"/>
      </linearGradient>
      <linearGradient id="hollyBand" x1="0" y1="0" x2="1" y2="0">
        <stop offset="0" stop-color="#b81a22"/>
        <stop offset="0.6" stop-color="#e8372c"/>
        <stop offset="1" stop-color="#c81e26"/>
      </linearGradient>
    </defs>
    <rect width="988" height="1200" fill="url(#snowfield)"/>
    <path d="M0,0 H988 V300 C820,300 700,390 600,460 C500,530 350,610 0,625 Z" fill="url(#starburst)"/>
    <path d="M0,235 C160,300 310,440 520,400 C700,360 800,170 988,160 V250 C840,250 720,360 600,440 C470,520 220,430 0,370 Z" fill="url(#emberBand)"/>
    <path d="M0,285 C160,350 320,470 530,430 C710,390 810,190 988,190 V318 C850,305 720,380 600,460 C480,535 220,470 0,415 Z" fill="url(#hollyBand)"/>
  </svg>

  <h1 class="title">Frostline Trophy</h1>
  <div class="year">2019</div>

  <div class="photo" role="img" aria-label="Photo of a rhythmic gymnast in a sparkling purple leotard lunging low with a ribbon streaming overhead"></div>

  <svg class="badge" viewBox="0 0 376 376" aria-hidden="true">
    <defs>
      <linearGradient id="goldRing" x1="0" y1="0" x2="0" y2="1">
        <stop offset="0" stop-color="#f5a623"/>
        <stop offset="0.5" stop-color="#fff04a"/>
        <stop offset="1" stop-color="#f5a623"/>
      </linearGradient>
    </defs>
    <circle cx="188" cy="188" r="184" fill="var(--holly-red)"/>
    <circle cx="188" cy="188" r="178" fill="url(#goldRing)"/>
    <circle cx="188" cy="188" r="156" fill="#8a9bb8"/>
    <circle cx="188" cy="188" r="152" fill="var(--royal-blue)"/>
  </svg>
  <div class="badge-text">
    <span class="badge-line1">INTERNATIONAL</span>
    <span class="badge-line2">Rhythmic</span>
    <span class="badge-line3">Gymnastics</span>
  </div>

  <div class="trophy" role="img" aria-label="Illustration of a golden trophy cup holding up the badge"></div>

  <svg class="dates-ribbon" viewBox="0 0 430 110" aria-hidden="true">
    <path d="M8,22 L405,4 L426,70 L410,102 L18,100 L30,60 Z" fill="#c99a3c"/>
    <path d="M12,26 L402,8 L420,70 L406,96 L22,96 L34,60 Z" fill="var(--ribbon-red)"/>
  </svg>
  <div class="dates">December 21 -23</div>

  <footer class="footer">
    <div class="hosted-by">HOSTED BY</div>
    <div class="host"><span>Venmarra Gymnastics</span><span class="host-mark"></span></div>
    <div class="venue">Los Angeles<span class="dot"></span>California<span class="dot"></span>USA</div>
    <div class="website">www.venmarragymnastics.com</div>
  </footer>
</main>
</body>
</html>
```